Varga Lillas Physiotherapy Business Card Vienna

We need a business card design for a newly created Physiotherapy company based in Vienna Austria.
We seek a simple, modern, minimalist design without too much color variation. The font should look young/fresh, but definitely not childish or so. Since we are a starting Business, we currently haven't got a logo, if you feel like a logo would fit your design, feel free to use one, but it's not necessary.
Target Market(s)
Healthcare, young and elderly people with mobility issues
Industry/Entity Type
Health And Wellness
Contact Information for Business Card
Name: Lilla Varga
Title description: Physiotherapist
Phone num: +43 664 5290 4816
e-mail: lilla.praxis@brelomail.com
Colors
Designer to choose colors to be used in the design.
Requirements
Must have
- Final design language must be in German, basically, the Title Description needs to be "Physiotherapeutin" the other details remain as in the English Language.
Nice to have
- Simple, modern, minimalist design
Should not have
- too many colors, Obvious use of a skeleton, skull, spline

```html
<!DOCTYPE html>
<html lang="de">
<head>
<meta charset="utf-8">
<title>Lilla Varga – Physiotherapeutin</title>
<link rel="stylesheet" href="https://fonts.googleapis.com/css2?family=Montserrat:wght@700&family=EB+Garamond:wght@400&display=swap">
<style>
  :root {
    --page-bg: #ffffff;
    --forest: #396a04;
    --lime: #cce58a;
    --mist: #e2e2e2;
    --ink: #3a6b04;
    --icon-glyph: #ffffff;
  }
  html, body {
    margin: 0;
    padding: 0;
    width: 1200px;
    height: 960px;
    overflow: hidden;
    background: var(--page-bg);
  }
  .canvas {
    position: relative;
    width: 1200px;
    height: 960px;
  }
  .business-card {
    position: absolute;
    left: 114px;
    top: 202px;
    width: 972px;
    height: 555px;
    display: block;
  }
  .card-name {
    font-family: "Montserrat", "Helvetica Neue", Arial, sans-serif;
    font-weight: 700;
    font-size: 94px;
    letter-spacing: 3px;
    fill: var(--ink);
  }
  .card-title {
    font-family: "EB Garamond", Garamond, Georgia, serif;
    font-size: 66px;
    fill: var(--ink);
  }
  .card-contact {
    font-family: Arial, "Helvetica Neue", Helvetica, sans-serif;
    font-size: 29px;
    fill: var(--ink);
  }
  .contact-icon-bg { fill: var(--forest); }
  .contact-icon-glyph { fill: var(--icon-glyph); }
  .contact-icon-line { fill: none; stroke: var(--forest); stroke-width: 1.6; }
</style>
</head>
<body>
<main class="canvas">
  <svg class="business-card" viewBox="0 0 1134 648" xmlns="http://www.w3.org/2000/svg" role="group" aria-label="Visitenkarte Lilla Varga, Physiotherapeutin">
    <rect class="card-base" x="0" y="0" width="1134" height="648" fill="var(--forest)"/>
    <path class="card-arc-accent" fill="var(--lime)"
          d="M0,107 C210,45 430,55 610,140 C810,240 950,440 1017,648 L0,648 Z"/>
    <path class="card-panel" fill="var(--mist)"
          d="M0,152 C210,102 420,110 585,185 C785,280 945,470 1017,648 L0,648 Z"/>

    <text class="card-name" x="33" y="409">LILLA VARGA</text>
    <text class="card-title" x="40" y="482">Physiotherapeutin</text>

    <g class="contact-phone">
      <circle class="contact-icon-bg" cx="86" cy="531" r="18"/>
      <path class="contact-icon-glyph"
            d="M78,537 c3,4 7,5 10,4 l2,-2 c1,-1 1,-2 0,-3 l-3,-2 c-1,-1 -2,0 -3,1 c-2,0 -5,-3 -5,-5 c1,-1 2,-2 1,-3 l-2,-3 c-1,-1 -2,-1 -3,0 l-2,2 c-1,3 1,8 5,11 z"/>
      <text class="card-contact" x="124" y="541">+43 664 5290 4816</text>
    </g>

    <g class="contact-email">
      <circle class="contact-icon-bg" cx="86" cy="574" r="18"/>
      <rect class="contact-icon-glyph" x="77" y="568" width="18" height="12" rx="1"/>
      <path class="contact-icon-line" d="M77.5,568.5 L86,575 L94.5,568.5 M77.5,579.5 L83.5,574 M94.5,579.5 L88.5,574"/>
      <text class="card-contact" x="122" y="584">lilla.praxis@brelomail.com</text>
    </g>
  </svg>
</main>
</body>
</html>
```